Business Card Design Project For Moving Company

Hello,

We need the business card to be 2 sided and we were thinking to use the logo on the front of the card (see file 1 attached) and the text "logo" (see file 2 attached) in the back of the card. We're looking for a powerful design that will help us build our brand, as our company is new.
We are a full service moving company (no storage) located in San Diego, CA, USA. The design should communicate to our potential customers that we have the highest level of service, customer satisfaction is our number one goal, our team is professional and efficient.

Thank you,

Dorn
Updates

Project Deadline Extended
Reason: We would like to have more time to provide feedback for the designs already submitted. Thank you, Dorn

Industry/Entity Type

Moving Company

Requirements
Must have
• Front of the card must have the following text and logo:
Haulbright, Inc
Residential And Commercial
Local And Long Distance
Address: 7312 Quillmont Rd, #146,
San Diego, CA, 92784
P: 855-372-LIFT (5438)
F: 858-529-4407
info@haul-bright.com
www.haul-bright.com

Back of the card must have the following text and text "logo" (file 2 attached):

The best compliment we can ever receive is a referral from our clients.

```html
<!DOCTYPE html>
<html lang="en">
<head>
<meta charset="utf-8">
<title>Haulbright, Inc – Business Card</title>
<link rel="stylesheet" href="https://fonts.googleapis.com/css2?family=Quicksand:wght@500;700&display=swap">
<style>
  :root {
    --card-white: #ffffff;
    --card-mist: #f1f1f1;
    --brand-red: #f23535;
    --panel-dark: #323232;
    --text-light: #ffffff;
    --divider: rgba(255, 255, 255, 0.75);
  }
  * { margin: 0; padding: 0; box-sizing: border-box; }
  html, body {
    width: 1200px;
    height: 719px;
    overflow: hidden;
    background: var(--card-white);
  }
  .card {
    position: relative;
    width: 1200px;
    height: 719px;
    font-family: "Quicksand", sans-serif;
    overflow: hidden;
  }
  .brand-area {
    position: absolute;
    left: 0; top: 0;
    width: 1200px; height: 324px;
    background: linear-gradient(135deg, var(--card-white) 0%, var(--card-mist) 50%, var(--card-white) 100%);
    display: flex;
    align-items: center;
    justify-content: center;
  }
  .brand-name {
    font-weight: 700;
    font-size: 150px;
    line-height: 1;
    color: var(--brand-red);
    letter-spacing: 2px;
    margin-top: 10px;
  }
  .accent-band {
    position: absolute;
    left: 0; top: 324px;
    width: 1200px; height: 50px;
    background: var(--brand-red);
  }
  .info-panel {
    position: absolute;
    left: 0; top: 374px;
    width: 1200px; height: 345px;
    background: var(--panel-dark);
    color: var(--text-light);
  }
  .company-details {
    position: absolute;
    left: 31px; top: 42px;
    font-weight: 500;
    font-size: 29px;
    line-height: 43px;
  }
  .contact-details {
    position: absolute;
    left: 31px; top: 200px;
    font-weight: 500;
    font-size: 23px;
    line-height: 38.5px;
  }
  .divider {
    position: absolute;
    left: 809px; top: 51px;
    width: 2px; height: 175px;
  }
  .web-details {
    position: absolute;
    left: 832px; top: 87px;
    font-weight: 500;
    font-size: 29px;
    line-height: 40px;
  }
</style>
</head>
<body>
  <div class="card">
    <header class="brand-area">
      <div class="brand-name">HAULBRIGHT</div>
    </header>
    <div class="accent-band"></div>
    <section class="info-panel">
      <div class="company-details">
        <p>Haulbright, Inc</p>
        <p>Residential And Commercial</p>
        <p>Local And Long Distance</p>
      </div>
      <div class="contact-details">
        <p>Address: 7312 Quillmont Rd, #146,</p>
        <p>San Diego, CA, 92784</p>
        <p>&nbsp;P: 855-372-LIFT (5438)&nbsp; F: 858-529-4407</p>
      </div>
      <svg class="divider" viewBox="0 0 2 175" preserveAspectRatio="none" aria-hidden="true">
        <line x1="1" y1="0" x2="1" y2="175" stroke="var(--divider)" stroke-width="2"/>
      </svg>
      <div class="web-details">
        <p>info@haul-bright.com</p>
        <p>www.haul-bright.com</p>
      </div>
    </section>
  </div>
</body>
</html>
```